Skincare Label Design Completion

I am starting up a skincare business and need the graphic design completed.

A previous designer started the project but was not able to finish. The logo, BC, letterhead, With Comp & gift voucher is complete. The BC, Letterhead, WC & GV need change of contact details. The BC needs a bit of wording transferred from front to back to look 'cleaner'. There are 15 product labels which need finishing; one is 95% complete, two are 80% complete, 11 have the groundwork done, one is not started at all. Pantone has been used, this may need changing to CMYK as printers prefer this.

PRODUCT NAMES, PACKAGING AND SPECS: All attached.

LOGO SYMBOL: Is a simple wheat image. The .ai file it can be 'pulled' out of is attached.

FRENCH TRANSLATION: The French translations of product names are to feature within the label. (Please see attached pdf's; look for the colour "stripe".)

PRODUCT DIFFERENTIATION: A unique colour is to be introduced to each product label that corresponds to the botanical ingredients found within. Ie: a light green to match Aloe Vera. That secondary colour is to feature (minimally) within that label. In the attached pdf's it's been placed as a contrasting colour stripe. Other ideas welcome. :)

BOTANICAL IMAGES: THIS IS NON-ESSENTIAL - A simple botanical image could feature on each label to correspond to the product name, instead of the colour stripe. Ie: A rosehip and rose flower on the Rosehip, Lavender and Jojoba Facial Cleanser.

COLOUR MATCHING: Each of the "secondary" colours (please see Product Differentiation) need to match each other as well as the logo colours. Some of the products are designed as combo's; ie, cleanser and moisturiser combo's. The colours for these combo's need to work together. The previous designer did a pdf of suggested secondary colours (attached), however these are mostly not in sync with the businesses' approach of earthy/simple/easy to look at/purity. A friend did a pdf of earthy green secondary colours (pdf attached entitled "Mon_Ciel_Clair_FC") and did a few creative suggestions for the label. The font, colours and design he used in the TOP LEFT label is the one I prefer but please use your creative license should you feel a different font would look better.

- LABEL INFO -
95% COMPLETED LABEL: See pdf "Mon_Ciel_Clair_FC"; top left label, product "Aloe & Lemon Myrtle Facial Cleanser". This needs the light writing at the top changed to Pantone Black 5C, and a colour decided upon for the stripe (see below for more info). The product info needs to be checked for accuracy against the word doc I've provided. (Some info has changed.) Note: All of the cleansers, moisturisers, the spray mist and the hand cream use this exact same label as above, only with a different colour stripe for differentiation and wording / title changed.

80% COMPLETED LABELS: See pdf "Mon Ciel Clair_label_ v4-1":
1) "Clarifying Macadamia & Green Clay Facial Masque" needs a different colour stripe selected/inserted, the light writing above the logo needs changed to Pantone Black 5C, the font needs to be made the same as the above label "Aloe & Lemon Myrtle Facial Cleanser", and the product info updated as per the product info word doc attached.
2) "Cocoa Butter & Apricot Body Cream" need a different colour stripe selected/inserted, the font changed to the same as "Aloe & Lemon Myrtle Facial Cleanser" label, and the product info updated as per the word doc attached. The other labels on that pdf can be dismissed.

INCOMPLETE LABELS: As noted above, the "Aloe & Lemon Myrtle" cleanser label is exactly the same for 7 other products (cleansers, moisturisers, spray mist and hand cream). The "Mon_Ciel_Clair_FC" can be used as the basis for these. Each one needs a different colour stripe for differentiation chosen and inserted, and the light wording above the logo changed to Black 5C.

The products "Sandalwood & Shea Butter Facial Exfoliating Cream", "Jojoba, Ylang Ylang & Vanilla Facial Exfoliant" and "Sweet Orange & Lavender Hand & Foot Scrub" all use exactly the same labels (one for jar, one for lid) as the Clarifying Macadamia & Green Clay masque. So you should be able to replicate this label for the other products. Each of these need the light writing above the logo changed to Black 5C and the colour stripes selected/inserted.

In the pdf "Mon Ciel Clair_label_ v4-1" the the 250mL bottle label has been completed. However that particular product was deleted. So using that label you can "pull out" the discontinued label wording and colour stripe, and replace it with the "Rosehip Body Lotion" label info. This also needs the light writing above the logo to be replaced with Pantone Black 5C, the colour stripe decided upon/inserted and the font to match with the above.

Only the lip balm has absolutely no work done on it. This will be just one small rectangular label.

Please note: this is not a re-branding so please stay true to the logo colours of Pantone 2717C, 4685C and Black 5C for the majority of the label. Secondary colour use is fine to match the botanicals.

Thank you so much in advance for your designs! :)

Maren.

Target Market(s)

Women aged 16 - 65+
Environmentally aware
Natural over chemical
Will spend a higher amount for a quality product
Women who want the best

Industry/Entity Type

Graphic Design

Font styles to use
Other font styles liked:
• Attached pdf "Mon_Ciel_Clair_FC" - top left label

Requirements
Must have
• Simple, clean lines, purity, natural / earthy colours.
• Secondary colours carefully chosen to reflect the botanical ingredients and to match the logo colours and each other.
• French translations on labels.
• LABELS MUST STAY WITH COLOURS MENTIONED IN BRIEF: PANTONE 2717C, 4685C, BLACK 5C - This is not a re-branding so please don't stray from using these colours for the majority of the label. (For secondary colour use to match botanicals, please use your creative license.)
Nice to have
• Botanical image on each label - non-essential
Should not have
• Nothing modern, harsh, stark or intense

```html
<!DOCTYPE html>
<html lang="en">
<head>
<meta charset="utf-8">
<title>Mon Ciel Clair – Aloe &amp; Lemon Myrtle Facial Cleanser Label</title>
<link rel="stylesheet" href="https://fonts.googleapis.com/css2?family=Source+Sans+3:ital,wght@0,400;0,600;1,600&family=Montserrat:wght@700&family=Cormorant+Garamond:ital,wght@1,500&display=swap">
<style>
  :root {
    --page-bg: #dde4e3;
    --leaf-green: #4f8d36;
    --leaf-green-deep: #2f6b25;
    --logo-green: #3d7a2f;
    --logo-rule: #b98870;
    --logo-text: #f1ecd2;
    --label-cream: #ebe8cc;
    --label-sage: #b9c1b1;
    --label-mist: #cfd5c8;
    --ink: #1c1a2a;
    --script-ink: #f4f4ee;
  }
  html, body {
    margin: 0;
    padding: 0;
    width: 901px;
    height: 1200px;
    overflow: hidden;
    background: var(--page-bg);
  }
  .canvas {
    position: relative;
    width: 901px;
    height: 1200px;
    background: var(--page-bg);
  }
  .label {
    position: absolute;
    left: 257px;
    top: 500px;
    width: 443px;
    height: 585px;
    overflow: hidden;
  }
  .label-artwork {
    position: absolute;
    inset: 0;
    background:
      radial-gradient(ellipse 120px 110px at 20px 175px, rgba(210,225,170,0.55), transparent 70%),
      radial-gradient(ellipse 90px 70px at 420px 40px, rgba(120,170,110,0.45), transparent 70%),
      radial-gradient(ellipse 110px 80px at 130px 320px, rgba(140,150,140,0.35), transparent 70%),
      linear-gradient(180deg,
        var(--leaf-green) 0%,
        #78a84e 18%,
        #c9d49a 30%,
        var(--label-cream) 40%,
        var(--label-mist) 56%,
        var(--label-sage) 72%,
        #a9b89c 88%,
        #8aa878 100%);
  }
  .logo-panel {
    position: absolute;
    left: 40px;
    top: 47px;
    width: 363px;
    height: 121px;
    background: var(--logo-green);
    box-sizing: border-box;
    border: 3px solid #5b9444;
  }
  .logo-panel::after {
    content: "";
    position: absolute;
    inset: 8px;
    border: 2px solid var(--logo-rule);
  }
  .logo-mark {
    position: absolute;
    left: 28px;
    top: 44px;
    width: 18px;
    height: 18px;
    border-radius: 50%;
    background: var(--logo-text);
  }
  .brand-name {
    position: absolute;
    left: 58px;
    top: 38px;
    margin: 0;
    font-family: "Source Sans 3", sans-serif;
    font-weight: 400;
    font-size: 24px;
    color: var(--logo-text);
  }
  .brand-tagline {
    position: absolute;
    left: 58px;
    top: 70px;
    margin: 0;
    font-family: "Source Sans 3", sans-serif;
    font-weight: 400;
    font-size: 12px;
    letter-spacing: 4px;
    color: var(--logo-text);
  }
  .range-statement {
    position: absolute;
    left: 0;
    right: 0;
    top: 200px;
    margin: 0;
    text-align: center;
    font-family: "Montserrat", sans-serif;
    font-weight: 700;
    font-size: 13px;
    line-height: 17px;
    letter-spacing: 4.5px;
    color: var(--ink);
  }
  .product-name {
    position: absolute;
    left: 0;
    right: 0;
    top: 295px;
    margin: 0;
    text-align: center;
    font-family: "Source Sans 3", sans-serif;
    font-weight: 400;
    font-size: 29px;
    line-height: 34px;
    color: var(--ink);
  }
  .skin-type {
    position: absolute;
    left: 0;
    right: 0;
    top: 393px;
    margin: 0;
    text-align: center;
    font-family: "Source Sans 3", sans-serif;
    font-style: italic;
    font-weight: 600;
    font-size: 15px;
    color: var(--ink);
  }
  .ingredients-note {
    position: absolute;
    left: 0;
    right: 0;
    top: 418px;
    margin: 0;
    text-align: center;
    font-family: "Source Sans 3", sans-serif;
    font-weight: 400;
    font-size: 13px;
    color: var(--ink);
  }
  .volume {
    position: absolute;
    left: 0;
    right: 0;
    top: 452px;
    margin: 0;
    text-align: center;
    font-family: "Source Sans 3", sans-serif;
    font-weight: 400;
    font-size: 18px;
    color: var(--ink);
  }
  .french-name {
    position: absolute;
    left: 8px;
    right: 8px;
    top: 508px;
    margin: 0;
    text-align: center;
    white-space: nowrap;
    font-family: "Cormorant Garamond", serif;
    font-style: italic;
    font-weight: 500;
    font-size: 18px;
    letter-spacing: 0;
    color: var(--script-ink);
  }
  .colour-stripe {
    position: absolute;
    left: 0;
    right: 0;
    bottom: 0;
    height: 44px;
    background: linear-gradient(180deg, #3f8a2c, var(--leaf-green-deep));
    border-top: 2px solid #e7efe0;
  }
</style>
</head>
<body>
  <main class="canvas">
    <section class="label">
      <div class="label-artwork" role="img" aria-label="Soft watercolour wash of green leaves and a lime slice behind the label text"></div>

      <div class="logo-panel">
        <span class="logo-mark"></span>
        <h1 class="brand-name">Mon Ciel Clair</h1>
        <p class="brand-tagline">MY CLEAR SKY</p>
      </div>

      <p class="range-statement">BOTANICAL FACE<br>&amp; BODY PRODUCTS<br>HAND-MADE WITH PASSION<br>&amp; CONSCIENCE</p>

      <h2 class="product-name">aloe &amp; lemon myrtle<br>facial cleanser</h2>

      <p class="skin-type">Especially for Normal to Oily Skin Types</p>
      <p class="ingredients-note">Containing Certified Organic Ingredients</p>
      <p class="volume">125ml</p>

      <p class="french-name" lang="fr">nettoyant pour le visage à l’aloès et au myrte citronné</p>

      <div class="colour-stripe"></div>
    </section>
  </main>
</body>
</html>
```